Mailer

Harbor Crest Partners, LLC
http://www.harborcrestpartnersllc.example/
412-863-2954
YOUR SUCCESS
You have an idea about where you want your business to go.  Need some help getting there? Are  you contemplating a transition to a new Broker Dealer, Producer Group or Custodian,  and/or interested in buying or selling a practice.
SOLUTIONS
Harbor Crest Partners, LLC is a consulting firm dedicated to  helping Finanial Advisors with their short term, and long term business affiliation and transition needs. W e interface with multple independent broker dealers and offer completely objective and unbiased guidance to help Financial Advisors find the perfect independent back office. Our services are free to you.

Industry/Entity Type
Business

```html
<!DOCTYPE html>
<html lang="en">
<head>
<meta charset="utf-8">
<title>Harbor Crest Partners, LLC — Mailer</title>
<link href="https://fonts.googleapis.com/css2?family=Open+Sans:ital,wght@0,400;0,700;1,400;1,700&display=swap" rel="stylesheet">
<style>
  :root {
    --bg: #ebe8e3;
    --navy: #0a2033;
    --blue: #1e93e6;
    --blue-light: #cfe6fb;
    --panel: #d9ebfb;
    --ink: #13283a;
    --white: #ffffff;
    --rule: #b9bcbf;
    --sky-top: #1d5fa8;
    --sky-mid: #6aa3d6;
    --snow: #eef3f8;
  }
  * { margin: 0; padding: 0; box-sizing: border-box; }
  html, body {
    width: 771px; height: 1200px; overflow: hidden;
    background: var(--bg);
    font-family: "Open Sans", Arial, sans-serif;
  }
  .canvas { position: relative; width: 771px; height: 1200px; }

  /* Front */
  .card-front {
    position: absolute; left: 41px; top: 15px;
    width: 690px; height: 534px; overflow: hidden;
    background: var(--white);
  }
  .hero-photo {
    position: absolute; inset: 0;
    background:
      radial-gradient(ellipse at 65% 55%, var(--snow) 0%, rgba(238,243,248,0.9) 35%, rgba(238,243,248,0) 70%),
      linear-gradient(115deg, var(--sky-top) 0%, var(--sky-mid) 28%, #c9dcee 45%, var(--snow) 65%, #d6e2ee 100%);
  }
  .front-curve { position: absolute; inset: 0; width: 690px; height: 534px; }
  .tagline {
    position: absolute; right: 32px; top: 348px;
    text-align: right; color: var(--ink);
    font-size: 28px; line-height: 32px; font-weight: 400;
  }
  .tagline-sub {
    position: absolute; left: 351px; top: 417px;
    color: var(--ink); font-size: 24px; font-style: italic;
  }
  .front-contact { position: absolute; left: 31px; top: 415px; color: var(--white); }
  .front-contact .company { font-size: 21px; line-height: 26px; }
  .front-contact .phone { font-size: 29px; font-weight: 700; line-height: 34px; margin-top: 8px; }
  .front-contact .web { font-size: 15px; line-height: 18px; }

  /* Back */
  .card-back {
    position: absolute; left: 41px; top: 600px;
    width: 690px; height: 534px; overflow: hidden;
    background: var(--white);
  }
  .info-panel {
    position: absolute; left: 0; top: 0;
    width: 334px; height: 441px; overflow: hidden;
    background: var(--panel);
  }
  .info-heading {
    position: absolute; left: 17px; width: 308px;
    font-size: 19px; line-height: 22px; font-weight: 400; color: var(--ink);
    border-bottom: 1.5px solid var(--ink); padding-bottom: 1px;
  }
  .info-heading.success { top: 25px; }
  .info-heading.solutions { top: 153px; }
  .info-body {
    position: absolute; left: 17px; width: 312px;
    font-size: 13.3px; line-height: 18.6px; color: var(--blue);
  }
  .info-body.success { top: 59px; }
  .info-body.solutions { top: 186px; }
  .info-body strong { color: var(--ink); font-style: italic; font-weight: 700; }
  .panel-curve { position: absolute; left: 0; top: 0; width: 334px; height: 441px; }
  .back-contact { position: absolute; left: 17px; top: 386px; color: var(--white); }
  .back-contact .phone { font-size: 24px; font-weight: 700; line-height: 28px; }
  .back-contact .web { font-size: 12px; line-height: 14px; }

  .mailing {
    position: absolute; left: 341px; top: 42px;
  }
  .mailing .company {
    display: inline-block; font-size: 17px; line-height: 22px;
    color: var(--ink); border-bottom: 1.5px solid var(--ink); padding-bottom: 3px;
  }
  .mailing .address { margin-top: 10px; font-size: 14px; line-height: 19px; color: var(--blue); }
  .mailing .email-label { margin-top: 7px; font-size: 14px; line-height: 17px; color: var(--ink); }
  .mailing .email { font-size: 14px; line-height: 17px; color: var(--blue); }
  .stamp-box {
    position: absolute; left: 579px; top: 22px;
    width: 91px; height: 100px; border: 1px solid var(--rule);
  }
  .address-line {
    position: absolute; left: 347px; width: 307px;
    border-top: 1px solid var(--rule);
  }
</style>
</head>
<body>
<div class="canvas">

  <section class="card-front">
    <div class="hero-photo" role="img" aria-label="Photo of a skier leaping off a snow cornice against a blue sky"></div>
    <svg class="front-curve" viewBox="0 0 690 534" aria-hidden="true">
      <path d="M0,355 C170,320 355,370 396,534 L0,534 Z" fill="var(--blue-light)"/>
      <path d="M0,366 C165,333 350,378 391,534 L0,534 Z" fill="var(--blue)"/>
      <path d="M0,396 C150,360 330,400 383,534 L0,534 Z" fill="var(--navy)"/>
    </svg>
    <p class="tagline">Some dream of success.<br>We make it happen.</p>
    <p class="tagline-sub">Fly Higher...</p>
    <div class="front-contact">
      <p class="company">Harbor Crest Partners, LLC</p>
      <p class="phone">412-863-2954</p>
      <p class="web">www.harborcrestpartnersllc.example</p>
    </div>
  </section>

  <section class="card-back">
    <div class="info-panel">
      <h2 class="info-heading success">YOUR SUCCESS</h2>
      <p class="info-body success">You have an idea about where you want your business to go. Need some help getting there? Are you contemplating a transition to a new Broker Dealer, Producer Group or Custodian, and/or interested in buying or selling a practice.</p>
      <h2 class="info-heading solutions">SOLUTIONS</h2>
      <p class="info-body solutions"><strong>Harbor Crest Partners, LLC</strong> is a consulting firm dedicated to helping Finanial Advisors with their short term, and long term business affiliation and transition needs. We interface with multple independent broker dealers and offer completely objective and unbiased guidance to help Financial Advisors find the perfect independent back office. Our services are free to you.</p>
      <svg class="panel-curve" viewBox="0 0 334 441" aria-hidden="true">
        <path d="M0,338 C125,320 238,352 264,441 L0,441 Z" fill="var(--blue)"/>
        <path d="M0,354 C120,340 230,368 256,441 L0,441 Z" fill="var(--navy)"/>
      </svg>
      <div class="back-contact">
        <p class="phone">412-863-2954</p>
        <p class="web">www.harborcrestpartnersllc.example</p>
      </div>
    </div>

    <div class="mailing">
      <p class="company">Harbor Crest Partners, LLC</p>
      <p class="address">1480 Larkspur Lane, NW<br>Brightwater, ST 20099</p>
      <p class="email-label">Email:</p>
      <p class="email">dana@harborcrestpartnersllc.example</p>
    </div>
    <div class="stamp-box"></div>
    <div class="address-line" style="top:241px"></div>
    <div class="address-line" style="top:284px"></div>
    <div class="address-line" style="top:327px"></div>
    <div class="address-line" style="top:370px"></div>
  </section>

</div>
</body>
</html>
```